Business Card / Appointment Card for Physician

On one side it should give the logo, address, and contact information, and on the other side it should br an Appointment card.

One Side:
Logo (see attached files)
Board Certified American Orthopedic Surgery

1487 Harrowgate Ave.
Suite KM7
Bronx, NY 10527
Tel: (718) 552 - 1948
Fax: (718) 552 - 7210

628 Fourth Ave.
Suite 42
New York, NY 10087
Tel: (212) 734 - 2815

Second Side:
Appointment
give them a choice of Bronx or Mahattan office
For:
Date:
Time:

If you are unable to keep your appointment, please call (718) 263-5102 24hrs in advance.

Target Market(s)

People that need orthopedic surgery

Industry/Entity Type

Business

Contact Information for Business Card

smart and attractive

Requirements
Must have
• logo
• contact information on one side, appointment information on the other

```html
<!DOCTYPE html>
<html lang="en">
<head>
<meta charset="utf-8">
<title>Whitford Orthopaedics – Business &amp; Appointment Card</title>
<link href="https://fonts.googleapis.com/css2?family=Exo+2:ital,wght@0,300;0,400;0,600;0,700;1,600&display=swap" rel="stylesheet">
<style>
  :root {
    --page-bg: #d9dbde;
    --card-bg: #ffffff;
    --card-shade: #eef0f3;
    --brand-blue: #1a6fb8;
    --navy: #123f7a;
    --sky: #3a9ad9;
    --green: #7cb342;
    --ink: #5b5e63;
    --rule: #7a7d82;
  }
  * { box-sizing: border-box; margin: 0; padding: 0; }
  html, body { width: 1200px; height: 1200px; overflow: hidden; }
  body {
    background: var(--page-bg);
    font-family: "Exo 2", "Segoe UI", sans-serif;
    position: relative;
  }
  .card {
    position: absolute;
    left: 180px;
    width: 840px;
    height: 480px;
    background: linear-gradient(150deg, var(--card-shade) 0%, var(--card-bg) 45%, var(--card-bg) 100%);
    box-shadow: 0 10px 30px rgba(0,0,0,.18);
  }
  .card--front { top: 80px; }
  .card--back  { top: 640px; }

  /* Front */
  .brand {
    position: absolute;
    right: 70px;
    top: 70px;
    display: flex;
    align-items: center;
    gap: 18px;
  }
  .brand__dot {
    width: 54px; height: 54px;
    border-radius: 50%;
    background: var(--sky);
  }
  .brand__name {
    font-weight: 700;
    font-size: 38px;
    color: var(--brand-blue);
    letter-spacing: .5px;
  }
  .front-text {
    position: absolute;
    right: 70px;
    top: 140px;
    text-align: right;
  }
  .specialty {
    font-weight: 600;
    font-size: 17px;
    color: var(--navy);
    letter-spacing: .3px;
  }
  .specialty .amp { color: var(--green); }
  .certification {
    font-weight: 300;
    font-size: 17px;
    color: var(--sky);
    margin-top: 4px;
    letter-spacing: .3px;
  }
  .office { margin-top: 34px; font-size: 20px; color: var(--ink); line-height: 1.6; }
  .office + .office { margin-top: 18px; }
  .label { color: var(--brand-blue); }

  /* Back */
  .appt-title {
    position: absolute;
    right: 70px; top: 56px;
    font-size: 28px;
    color: var(--brand-blue);
    letter-spacing: .5px;
  }
  .appt-form {
    position: absolute;
    left: 70px; right: 70px; top: 130px;
    font-size: 19px;
    color: var(--ink);
  }
  .field-row { display: flex; align-items: baseline; margin-bottom: 26px; }
  .field { display: flex; align-items: baseline; flex: 1; }
  .field + .field { margin-left: 18px; }
  .dots { flex: 1; border-bottom: 2px dotted var(--rule); margin-left: 6px; transform: translateY(-4px); }
  .office-choice { font-size: 22px; margin: 14px 0 18px; }
  .blank-line { border-bottom: 2px dotted var(--rule); height: 24px; margin-bottom: 30px; }
  .notice {
    font-style: italic;
    font-weight: 600;
    font-size: 18px;
    color: var(--brand-blue);
  }
</style>
</head>
<body>

  <section class="card card--front">
    <div class="brand">
      <span class="brand__dot"></span>
      <span class="brand__name">DANIEL R. WHITFORD MD PC</span>
    </div>
    <div class="front-text">
      <p class="specialty">ORTHOPAEDIC SURGERY <span class="amp">&amp;</span> SPORTS MEDICINE</p>
      <p class="certification">BOARD CERTIFIED AMERICAN ORTHOPEDIC SURGERY</p>
      <div class="office">
        <p><span class="label">Tel:</span> (212) 734 - 2815</p>
        <p>628 Fourth Ave. Suite 42, New York, NY 10087</p>
      </div>
      <div class="office">
        <p><span class="label">Tel:</span> (718) 552 - 1948 | <span class="label">Fax:</span> (718) 552 - 7210</p>
        <p>1487 Harrowgate Ave. Suite KM7, Bronx, NY 10527</p>
      </div>
    </div>
  </section>

  <section class="card card--back">
    <h2 class="appt-title">YOUR NEXT APPOINTMENT</h2>
    <div class="appt-form">
      <div class="field-row">
        <div class="field">Date:<span class="dots"></span></div>
        <div class="field">Time:<span class="dots"></span></div>
      </div>
      <div class="field-row">
        <div class="field">Date:<span class="dots"></span></div>
        <div class="field">Time:<span class="dots"></span></div>
      </div>
      <p class="office-choice">give them a choice of Bronx or Mahattan office For:</p>
      <div class="blank-line"></div>
      <p class="notice">If you are unable to keep your appointment, please call (718) 263-5102 24hrs in advance.</p>
    </div>
  </section>

</body>
</html>
```